Brindlecove Flood Restoration needing website

Hi Team

We are looking for a 4 or 5 page website containing
1: Home
2: Services
3: Gallery
4: Equipment Hire
5 Contact Us

Would want the front page to be a big call to action. Someones house has just flooded...they're highly stressed and we just want to let them know straight away that we can assist them

Some call to action would be great.

"Wet Carpets??"

"Washing machine just overflowed??"

"Burst pipe?"

"We're here to help!!"

Would be wanting a scrolling banner type homepage with images of flooded houses, heavy rain, a mother in shock that the house has been flooded by an overflowing washing machine, someone taking an emergency call with text saying that we are there to take your call 24/7 365 days a year

Target Market(s)

insurance companies and home owners

Industry/Entity Type

Hire

Coding

Coded - Design and coding required

Number of Pages Required

5+ page

Requirements
Must have
• 24/7 emergency contact number on home page (0498215763)
• 4 photos on banner on home page
• Equipment Hire Page should include images and brief description of these 3 products
• http://www.ptkdirect.example.com.au/prod458.htm
• http://www.gustline-gear.example.com.au/product/mistral-breeze-fan/
• http://www.vendrasuck.example.com.au/carpet/carpet-extractor-harrier-xv-x-vi-x-vii
• SERVICES OFFERED ARE:
• 24/7 Emergnecy Flood Restoration
• Insurance Claims
• Structural Drying
• Sub Floor Drying
• Supply and installation of drying equipment
• Professional Carpet and underlay installation
Nice to have
• Some other websites we like
• www.kelbyleakfixers.example.com.au
• www.summitrecoverywashing.example.com.au/flood-water-damage-restoration
• http://www.pelhamrecovery.example.com.au/
• http://www.dampfixnational.example.com.au/
Should not have
• not looking for an all white background.

```html
<!DOCTYPE html>
<html lang="en">
<head>
<meta charset="utf-8">
<title>Brindlecove Flood Restoration</title>
<link rel="stylesheet" href="https://fonts.googleapis.com/css2?family=Maven+Pro:wght@400;500;700&family=Roboto:wght@400;500&display=swap">
<style>
:root{
  --blue:#1a8fd0;
  --blue-dark:#0c6fa8;
  --blue-deep:#0b3e57;
  --cyan:#2fb3ea;
  --ink:#3a3a3a;
  --muted:#7a7a7a;
  --footer:#2a2a2a;
  --footer-bar:#1e1e1e;
  --white:#ffffff;
}
*{margin:0;padding:0;box-sizing:border-box}
html,body{width:1200px;height:2528px;overflow:hidden}
body{position:relative;background:var(--white);font-family:'Roboto',sans-serif;color:var(--ink)}
.abs{position:absolute}

/* header */
.site-header{position:absolute;left:0;top:0;width:1200px;height:68px;background:rgba(8,30,40,.55);z-index:5}
.brand{position:absolute;left:93px;top:14px;display:flex;align-items:center;gap:10px;color:var(--white);font-family:'Maven Pro',sans-serif;font-weight:700;font-size:17px;line-height:19px;letter-spacing:.3px}
.brand-dot{width:34px;height:34px;border-radius:50%;background:var(--cyan);flex:none}
.main-nav{position:absolute;left:388px;top:20px;display:flex;gap:8px;font-family:'Roboto',sans-serif;font-size:16px;white-space:nowrap}
.main-nav a{color:var(--white);text-decoration:none;padding:4px 10px}
.main-nav a.active{background:var(--blue-dark)}
.header-phone{position:absolute;right:93px;top:6px;height:52px;width:214px;background:var(--blue-dark);border-radius:0 0 12px 12px;display:flex;align-items:center;gap:8px;padding-left:10px;color:var(--white);font-family:'Maven Pro',sans-serif;font-size:23px;font-weight:500;white-space:nowrap}

/* hero */
.hero{position:absolute;left:0;top:0;width:1200px;height:690px}
.hero-photo{position:absolute;inset:0;height:650px;background:linear-gradient(160deg,#2d5a6b 0%,#3f7f92 35%,#5fa9c4 60%,#1f86b8 100%)}
.hero-wave{position:absolute;left:0;top:560px}
.hero-band{position:absolute;left:0;top:276px;width:742px;height:142px;background:rgba(10,45,60,.55);border-top:3px solid var(--cyan)}
.hero-title{position:absolute;left:93px;top:314px;font-family:'Maven Pro',sans-serif;font-weight:500;font-size:38px;color:var(--white);white-space:nowrap}
.hero-sub{position:absolute;left:93px;top:356px;font-family:'Maven Pro',sans-serif;font-size:28px;color:var(--cyan)}
.slider-dots{position:absolute;right:8px;top:310px;display:flex;flex-direction:column;gap:6px}
.slider-dots span{width:9px;height:9px;border-radius:50%;border:1.5px solid var(--cyan)}
.slider-dots span.on{background:var(--cyan)}

/* welcome */
.welcome{position:absolute;left:93px;top:752px;width:640px}
.section-title{font-family:'Maven Pro',sans-serif;font-size:34px;color:#6a6a6a;font-weight:400;white-space:nowrap}
.welcome .section-title{font-size:30px}
.section-title strong{color:var(--blue);font-weight:700}
.section-title .accent{color:var(--blue)}
.title-rule{width:90px;height:2px;background:var(--blue);margin:12px 0 28px}
.welcome p{font-size:13.5px;line-height:27px;color:var(--muted)}
.welcome-divider{position:absolute;left:753px;top:760px;height:218px;border-left:1px dashed #c9c9c9}
.emergency{position:absolute;left:785px;top:760px;width:320px}
.emergency-head{display:flex;gap:10px;height:78px}
.emergency-head svg{flex:none}
.emergency-head h3{font-family:'Maven Pro',sans-serif;font-weight:400;font-size:23px;color:#777;letter-spacing:1px;line-height:26px;margin-top:10px;white-space:nowrap}
.emergency-head h3 b{display:block;color:var(--blue);font-weight:700;letter-spacing:0}
.emergency p{margin-top:-4px;text-indent:96px;font-size:13px;line-height:21px;color:var(--muted)}
.call-box{position:absolute;left:785px;top:918px;width:270px;height:62px;background:var(--blue-dark);border-radius:10px 0 0 10px;color:var(--white);padding:6px 0 0 16px;white-space:nowrap}
.call-box small{display:block;font-size:14px;letter-spacing:.5px}
.call-box span{font-family:'Maven Pro',sans-serif;font-size:31px;line-height:34px;font-weight:500}
.call-avatar{position:absolute;left:1020px;top:904px;width:86px;height:86px;border-radius:50%;border:3px solid var(--blue-dark);background:linear-gradient(#e6d9cf,#c8b6a6)}

/* services */
.services{position:absolute;left:0;top:1062px;width:1200px;height:486px;background:linear-gradient(180deg,#1b8ccb,#1a94d4 60%,#178bc9)}
.services-notch{position:absolute;left:540px;top:1010px}
.services h2{position:absolute;left:0;top:98px;width:1200px;text-align:center;font-family:'Maven Pro',sans-serif;font-weight:400;font-size:34px;color:var(--white)}
.services h2 b{font-weight:700}
.services-intro{position:absolute;left:140px;top:160px;width:920px;text-align:center;font-size:13.5px;line-height:24px;color:var(--white)}
.service-list{position:absolute;left:93px;top:258px;width:1012px;display:flex}
.service{flex:none;text-align:center;color:var(--white);font-family:'Maven Pro',sans-serif;font-size:18px;line-height:21px;border-right:1px dashed rgba(255,255,255,.45);height:150px}
.service:last-child{border-right:0}
.service svg{display:block;margin:0 auto 10px}
.service.current{color:#bfe6fa}

/* gallery */
.gallery-title{position:absolute;left:0;top:1620px;width:1200px;text-align:center}
.view-all{position:absolute;left:978px;top:1625px;width:128px;height:40px;border:2px solid var(--blue);color:var(--blue);font-size:15px;font-weight:500;display:flex;align-items:center;justify-content:center}
.tile{position:absolute}
.tile-frame{position:absolute;inset:12px;border:3px solid rgba(255,255,255,.85)}

/* footer */
.site-footer{position:absolute;left:0;top:2241px;width:1200px;height:223px;background:var(--footer);color:#cfcfcf}
.footer-brand{position:absolute;left:93px;top:42px;display:flex;align-items:center;gap:8px;color:#7fd0f5;font-family:'Maven Pro',sans-serif;font-weight:700;font-size:15px;line-height:17px}
.footer-brand i{width:28px;height:28px;border-radius:50%;background:var(--cyan);flex:none}
.social{position:absolute;left:124px;top:103px;display:flex;gap:5px}
.social span{width:27px;height:27px;background:#4a4a4a}
.footer-col h4{font-size:13px;font-weight:500;letter-spacing:1px;color:#e6e6e6;margin-bottom:20px;white-space:nowrap}
.footer-col li{list-style:none;font-size:12px;line-height:27px;color:#bdbdbd}
.footer-col.contact li{display:flex;align-items:flex-start;gap:12px;margin-bottom:6px;line-height:17px}
.newsletter-input{width:233px;height:40px;border:1px solid #555;background:#2e2e2e;color:#888;font-size:12px;display:flex;align-items:center;padding-left:12px;gap:8px}
.newsletter-btn{margin-top:6px;width:128px;height:40px;background:var(--blue);color:var(--white);font-size:15px;font-weight:500;display:flex;align-items:center;justify-content:center;border:1px solid #4fb5ea}
.footer-bar{position:absolute;left:0;top:2464px;width:1200px;height:64px;background:var(--footer-bar);color:#ddd;font-size:13px;letter-spacing:.8px;text-align:center;line-height:64px}
</style>
</head>
<body>

<section class="hero">
  <div class="hero-photo" role="img" aria-label="Photo of a stressed woman in a laundry room beside an overflowing washing machine"></div>
  <svg class="hero-wave" width="1200" height="130" viewBox="0 0 1200 130">
    <path d="M0 30 C300 90 500 110 600 110 C750 110 950 60 1200 50 L1200 130 L0 130 Z" fill="#2fb3ea" opacity=".55"/>
    <path d="M0 50 C300 110 500 115 600 115 C760 115 950 85 1200 75 L1200 130 L0 130 Z" fill="#ffffff"/>
    <path d="M565 110 Q600 90 635 110 Q612 128 600 128 Q588 128 565 110 Z" fill="#2fb3ea"/>
    <path d="M591 108 L600 116 L609 108" fill="none" stroke="#fff" stroke-width="3"/>
  </svg>
  <div class="hero-band"></div>
  <h1 class="hero-title">Washing machine just overflowed??</h1>
  <p class="hero-sub">We're here to help!!</p>
  <div class="slider-dots"><span class="on"></span><span></span><span></span><span></span></div>
</section>

<header class="site-header">
  <div class="brand"><span class="brand-dot"></span><span>Brindlecove<br>Flood Restoration</span></div>
  <nav class="main-nav">
    <a class="active" href="#">Home</a><a href="#">Services</a><a href="#">Gallery</a><a href="#">Equipment Hire</a><a href="#">Contact Us</a>
  </nav>
  <div class="header-phone">
    <svg width="40" height="40" viewBox="0 0 40 40"><circle cx="20" cy="20" r="17" fill="none" stroke="#fff" stroke-width="2"/><text x="20" y="25" text-anchor="middle" font-family="Maven Pro, sans-serif" font-size="12" fill="#fff" font-weight="700">24/7</text></svg>
    <span>049 8215 763</span>
  </div>
</header>

<section class="welcome">
  <h2 class="section-title">Welcome to <strong>Brindlecove</strong> <span class="accent">Flood Restoration</span></h2>
  <div class="title-rule"></div>
  <p>Lorem ipsum dolor sit amet, consectetur adipiscing edu e elit, sed do eiusmod tempor incididunt ut labore et dolore magna aliqua. Ut enim minim veniam, quis nostrud exercitation ullamco laboris nisi ut aliquip erex ea commodo consequat. Duis aut irure dolor in reprehendit in voluptate velit esse cillum dolore eu fugiat nulla pariatur. Excepteur sin in occaecat cupidatat non prident, edu sunt in culpa qui officia deserunt laboris nisi ut consectetur adipiscing edu.</p>
</section>
<div class="welcome-divider"></div>

<aside class="emergency">
  <div class="emergency-head">
    <svg width="86" height="80" viewBox="0 0 90 86"><circle cx="45" cy="43" r="36" fill="none" stroke="#1a8fd0" stroke-width="4"/><path d="M12 20 l10 -8 l8 10 l-6 5 q4 10 12 16 l5 -6 l10 8 l-8 10 q-22 -6 -31 -35 Z" fill="#1a8fd0" transform="translate(-4 -4) scale(.9)"/><text x="50" y="50" text-anchor="middle" font-family="Maven Pro, sans-serif" font-size="21" font-weight="700" fill="#1a8fd0">24/7</text></svg>
    <h3>24/7 Emergnecy <b>Flood Restoration</b></h3>
  </div>
  <p>Lorem ipsum dolor sit amet, edusi consectetur adipiscing edu e elit, sed do eiusmod tempor incididunt ut labore.</p>
</aside>
<div class="call-box"><small>CALL US ON</small><span>049 8215 763</span></div>
<div class="call-avatar" role="img" aria-label="Photo of a call centre operator wearing a headset"></div>

<section class="services" role="region" aria-label="Our Services">
  <div class="abs" style="inset:0;background:radial-gradient(ellipse at 35% 30%,rgba(255,255,255,.12),transparent 60%)" role="img" aria-label="Faint photo of a carpet cleaning machine"></div>
  <h2>Our <b>Services</b></h2>
  <p class="services-intro">Lorem ipsum dolor sit amet, consectetur adipiscing edu e elit, sed do eiusmod tempor incididunt ut labore et dolore magna aliqua. Ut enim minim veniam, quis nostrud exercitation ullamco laboris nisi ut psum dolor sit amet, consectetur adipiscing edu e elit</p>
  <div class="service-list">
    <div class="service" style="width:160px">
      <svg width="90" height="84" viewBox="0 0 90 84" fill="none" stroke="#fff" stroke-width="4"><path d="M8 40 Q45 -10 82 40 Q72 32 63 40 Q54 32 45 40 Q36 32 27 40 Q18 32 8 40 Z" fill="#fff"/><path d="M45 40 V72 Q45 80 37 80 Q30 80 30 72"/></svg>
      Insurance<br>Claims
    </div>
    <div class="service" style="width:192px">
      <svg width="90" height="84" viewBox="0 0 90 84" fill="none" stroke="#fff" stroke-width="3"><rect x="18" y="14" width="30" height="66"/><rect x="48" y="40" width="24" height="40"/><path d="M26 14 V4 M38 14 V6"/><g fill="#fff" stroke="none"><rect x="24" y="22" width="6" height="8"/><rect x="36" y="22" width="6" height="8"/><rect x="24" y="38" width="6" height="8"/><rect x="36" y="38" width="6" height="8"/><rect x="24" y="54" width="6" height="8"/><rect x="36" y="54" width="6" height="8"/><rect x="54" y="48" width="5" height="7"/><rect x="62" y="48" width="5" height="7"/><rect x="54" y="62" width="5" height="7"/><rect x="62" y="62" width="5" height="7"/></g></svg>
      Structural<br>Drying
    </div>
    <div class="service current" style="width:190px">
      <svg width="100" height="84" viewBox="0 0 100 84" fill="none" stroke="#bfe6fa" stroke-width="3"><path d="M24 20 H76 L92 76 H8 Z"/><path d="M34 30 H66 L74 66 H26 Z"/><path d="M24 20 L34 30 M76 20 L66 30 M8 76 L26 66 M92 76 L74 66"/></svg>
      Sub Floor<br>Drying
    </div>
    <div class="service" style="width:268px">
      <svg width="100" height="84" viewBox="0 0 100 84" fill="none" stroke="#fff" stroke-width="3"><path d="M14 14 H62 Q84 14 84 32 Q84 50 62 50 H52 L48 78 H36 L40 50 H14 Z"/><circle cx="66" cy="32" r="10"/><path d="M14 22 H30 M14 30 H30 M14 38 H30"/></svg>
      Supply &amp; installation of<br>drying equipment
    </div>
    <div class="service" style="width:202px">
      <svg width="100" height="84" viewBox="0 0 100 84" fill="none" stroke="#fff" stroke-width="3"><path d="M30 62 L82 22 L92 36 L48 72 Z"/><circle cx="30" cy="50" r="16" fill="#fff"/><circle cx="30" cy="50" r="6" stroke="#1a94d4"/><path d="M16 60 L40 76 L48 72"/></svg>
      Professional Carpet &amp;<br>underlay installation
    </div>
  </div>
</section>
<svg class="services-notch" width="120" height="96" viewBox="0 0 120 96">
  <path d="M0 53 L16 53 Q60 -12 104 53 L120 53 Z" fill="#1b8ccb"/>
  <circle cx="60" cy="50" r="40" fill="#fff"/>
  <circle cx="60" cy="50" r="34" fill="none" stroke="#1a8fd0" stroke-width="3"/>
  <circle cx="60" cy="50" r="20" fill="#1a8fd0"/>
</svg>

<h2 class="section-title gallery-title">Our <strong>Gallery</strong></h2>
<div class="view-all">View All</div>

<div class="tile" style="left:93px;top:1714px;width:320px;height:226px;background:linear-gradient(160deg,#5fa6c9,#2f7fae)" role="img" aria-label="Photo of a flooded living room with a sofa"><div class="tile-frame"></div></div>
<div class="tile" style="left:421px;top:1714px;width:356px;height:463px;background:linear-gradient(180deg,#9cc9e8 0%,#b89a82 35%,#6f7a5a 55%,#4c4f46 75%,#3a3a36 100%)" role="img" aria-label="Photo of a suburban house surrounded by floodwater"></div>
<div class="tile" style="left:787px;top:1714px;width:318px;height:226px;background:linear-gradient(160deg,#e8e8e6,#b9b6b0 60%,#6d6a66)" role="img" aria-label="Photo of a flooded hallway with a staircase"></div>
<div class="tile" style="left:93px;top:1950px;width:320px;height:227px;background:linear-gradient(135deg,#3d5a2c,#6f8f42 40%,#c9567a 70%,#e7a54a)" role="img" aria-label="Photo of a woman under a colourful umbrella in heavy rain"></div>
<div class="tile" style="left:787px;top:1950px;width:318px;height:227px;background:linear-gradient(160deg,#cfc9c0,#9d8f80 50%,#6b6560)" role="img" aria-label="Photo of a floor cleaning machine on carpet"></div>

<footer class="site-footer">
  <div class="footer-brand"><i></i><span>Brindlecove<br>Flood Restoration</span></div>
  <div class="social"><span></span><span></span><span></span><span></span></div>
  <div class="footer-col abs" style="left:350px;top:48px">
    <h4>QUICK LINKS</h4>
    <ul><li>&gt;&gt; Home</li><li>&gt;&gt; Services</li><li>&gt;&gt; Gallery</li><li>&gt;&gt; Equipment Hire</li></ul>
  </div>
  <div class="footer-col contact abs" style="left:553px;top:48px">
    <h4>CONTACT US</h4>
    <ul>
      <li><svg width="12" height="16" viewBox="0 0 12 16"><path d="M6 0 A6 6 0 0 1 12 6 C12 10 6 16 6 16 C6 16 0 10 0 6 A6 6 0 0 1 6 0 Z" fill="#cfcfcf"/><circle cx="6" cy="6" r="2" fill="#2a2a2a"/></svg><span>48 Tidewell Avenue<br>Marlow Heath, NY 08096</span></li>
      <li style="margin-top:10px"><svg width="12" height="14" viewBox="0 0 12 14"><path d="M1 1 L4 0 L6 4 L4 5 Q5 8 8 9 L9 7 L12 9 L11 12 Q3 12 1 1 Z" fill="#cfcfcf"/></svg><span>049 8215 763</span></li>
      <li style="margin-top:10px"><svg width="13" height="10" viewBox="0 0 13 10"><rect width="13" height="10" fill="#cfcfcf"/><path d="M0 0 L6.5 5 L13 0" fill="none" stroke="#2a2a2a" stroke-width="1.2"/></svg><span>customerservice@brindlecove.example.com</span></li>
    </ul>
  </div>
  <div class="footer-col abs" style="left:872px;top:48px">
    <h4>SUBSCRIBE OUR NEWSLETTER</h4>
    <div class="newsletter-input"><svg width="12" height="9" viewBox="0 0 12 9"><rect width="12" height="9" fill="#888"/><path d="M0 0 L6 4.5 L12 0" fill="none" stroke="#2e2e2e"/></svg>Email</div>
    <div class="newsletter-btn">Submit</div>
  </div>
</footer>
<div class="footer-bar">© Brindlecove Flood Restoration. &nbsp;All rights reserved.</div>

</body>
</html>
```